Brand-new Pediatric Dental Practice needs a website

We are a brand-new dental practice that will specialize in treating children. We want a gorgeous and easily navigable dental practice website that would make a good first impression to potential patients and their parents. It should be modern, SEO-friendly, mobile responsive, and optimized to win new patients.

Target Market(s)

Parents

Industry/Entity Type

Healthcare/Dentistry

Coding

Coded - Design and coding required

Number of Pages Required

4 page

Requirements
Must have
• Use the Wix website building platform. 4 pages: home, meet our dentists, services, contact us
Nice to have
• has a link to our facebook, instagram

```html
<!DOCTYPE html>
<html lang="en">
<head>
<meta charset="utf-8">
<title>Bramble Bay Dental</title>
<link rel="stylesheet" href="https://fonts.googleapis.com/css2?family=Roboto:wght@400;500;700;900&display=swap">
<style>
:root{
  --green:#5cbf73;
  --green-dark:#45a85d;
  --green-soft:#7fd08f;
  --ink:#222;
  --muted:#555;
  --white:#fff;
  --footer:#f2f2f2;
  --line:#d6d6d6;
}
*{box-sizing:border-box;margin:0;padding:0}
html,body{width:1200px;height:3480px;overflow:hidden}
body{font-family:'Roboto',sans-serif;color:var(--ink);background:var(--white);position:relative}
.abs{position:absolute}
.btn{display:inline-flex;align-items:center;justify-content:center;gap:8px;background:var(--green);color:var(--white);font-weight:500;font-size:15px;border-radius:3px;text-decoration:none}
.btn .arrow{width:18px;height:18px;border-radius:50%;background:var(--white);color:var(--green);display:inline-flex;align-items:center;justify-content:center;font-size:12px;font-weight:900}

/* header */
.site-header{top:0;left:0;width:1200px;height:88px}
.brand{left:112px;top:14px;display:flex;flex-direction:column;align-items:center;gap:4px}
.brand-mark{width:30px;height:30px;border-radius:50%;background:var(--green)}
.brand-name{font-size:17px;font-weight:500;color:var(--ink)}
.login{left:812px;top:26px;display:flex;align-items:center;gap:10px;font-size:16px;font-weight:500}
.login-icon{width:26px;height:26px;border-radius:50%;background:var(--green)}
.book-top{left:928px;top:18px;width:160px;height:50px;font-size:16px}

/* nav */
.main-nav{top:88px;left:0;width:1200px;height:60px;background:var(--green);display:flex;justify-content:center;align-items:center;gap:62px}
.main-nav a{color:var(--white);font-size:17px;font-weight:500;text-decoration:none}

/* hero */
.hero{top:148px;left:0;width:1200px;height:484px;background:linear-gradient(90deg,#3b3f46 0%,#8b8f96 45%,#d8d4d0 75%,#c9c3bd 100%)}
.hero-copy{left:112px;top:76px;width:420px;color:var(--white)}
.hero-title{font-size:50px;font-weight:700;line-height:1.12}
.hero-text{margin-top:22px;font-size:17px;line-height:1.55}
.hero .btn{margin-top:28px;width:146px;height:46px}
.dots{left:568px;top:452px;display:flex;gap:8px}
.dots i{width:10px;height:10px;border-radius:50%;background:rgba(255,255,255,.6)}
.dots i.on{background:var(--white)}

/* about */
.about-photo{left:112px;top:712px;width:400px;height:528px;border-radius:6px;background:linear-gradient(160deg,#e9d8c8,#c7a58a 60%,#f1ebe4)}
.about-inset{left:452px;top:996px;width:264px;height:264px;border-radius:50%;border:8px solid var(--white);background:linear-gradient(160deg,#f3f0ec,#d6c7bb);box-shadow:0 4px 14px rgba(0,0,0,.15)}
.about-copy{left:646px;top:796px;width:520px}
.section-title{font-size:48px;font-weight:700;color:var(--ink)}
.about-text{margin-top:16px;font-size:18px;line-height:1.55;text-align:justify;color:var(--ink)}
.about-copy .btn{margin-top:26px;width:150px;height:48px}

/* services */
.services{top:1328px;left:0;width:1200px;height:632px;background:linear-gradient(135deg,var(--green-dark),var(--green-soft) 50%,var(--green-dark))}
.services .section-title{position:absolute;top:40px;width:1200px;text-align:center;color:var(--white)}
.service-card{width:356px;height:120px;background:var(--white);border-radius:4px;display:flex;align-items:center;padding:0 18px;gap:22px;box-shadow:0 2px 8px rgba(0,0,0,.12)}
.service-icon{flex:none;width:78px;height:78px}
.service-body{text-align:center;flex:1}
.service-name{font-size:18px;font-weight:700}
.service-text{margin-top:6px;font-size:15px;line-height:1.35;color:var(--muted)}

/* dentists */
.dentists-title{top:2004px;left:0;width:1200px;text-align:center}
.dentist{width:300px;text-align:center}
.dentist-photo{width:220px;height:220px;border-radius:50%;margin:0 auto;background:linear-gradient(160deg,#e6ecef,#b9c7cf);box-shadow:0 3px 10px rgba(0,0,0,.15)}
.dentist-name{margin-top:26px;font-size:26px;font-weight:700}
.dentist-role{margin-top:6px;font-size:17px;color:var(--muted)}
.dentist .btn{margin-top:14px;width:150px;height:40px;font-size:14px}

/* contact */
.contact-title{top:2518px;left:0;width:1200px;text-align:center}
.contact-col{width:420px;text-align:center}
.contact-col h3{font-size:24px;font-weight:500}
.contact-col p{margin-top:16px;font-size:16px;color:var(--muted)}
.contact-divider{left:628px;top:2612px;width:1px;height:150px;background:var(--line)}

/* map */
.map{left:112px;top:2808px;width:968px;height:312px;background:linear-gradient(135deg,#eef0e6,#dfe6d6 50%,#f0ede2)}
.map-toggle{left:132px;top:2826px;display:flex;background:var(--white);box-shadow:0 1px 4px rgba(0,0,0,.25)}
.map-toggle span{padding:8px 18px;font-size:15px}
.map-toggle span + span{color:#888}
.map-zoom{left:1030px;top:3040px;width:34px;height:64px;background:var(--white);box-shadow:0 1px 4px rgba(0,0,0,.25);display:flex;flex-direction:column;align-items:center;justify-content:space-around;font-size:20px;color:#666}

/* footer */
.site-footer{top:3180px;left:0;width:1200px;height:300px;background:var(--footer)}
.footer-brand{left:140px;top:40px;display:flex;flex-direction:column;align-items:center;gap:6px}
.footer-brand .brand-mark{width:44px;height:44px}
.social{display:flex;gap:10px;margin-top:6px}
.social i{width:24px;height:24px;border-radius:50%;background:var(--ink)}
.footer-col h4{font-size:22px;font-weight:700;margin-bottom:12px}
.footer-col p{font-size:13px;line-height:1.9;color:var(--ink)}
.footer-form{left:820px;top:24px;width:260px}
.field{background:var(--white);height:40px;margin-bottom:12px;font-size:13px;padding:12px 12px;color:var(--muted)}
.field.tall{height:90px}
.footer-form .btn{float:right;width:88px;height:32px;font-size:14px}
.copyright{top:3454px;left:0;width:1200px;text-align:center;font-size:12px;color:var(--muted)}
</style>
</head>
<body>

<header class="site-header abs">
  <div class="brand abs"><span class="brand-mark"></span><span class="brand-name">Bramble Bay</span></div>
  <div class="login abs"><span class="login-icon"></span>Log In</div>
  <a class="btn book-top abs" href="#">Book Appointment</a>
</header>

<nav class="main-nav abs">
  <a href="#">Home</a><a href="#">About</a><a href="#">Our Dentists</a><a href="#">Services</a><a href="#">Contact us</a>
</nav>

<section class="hero abs" role="img" aria-label="Photo of a dentist examining a smiling patient">
  <div class="hero-copy abs">
    <h1 class="hero-title">Healthy Smile Teeth Healthy Life</h1>
    <p class="hero-text">Dentistry, also known as dental medicine and oral medicine, is a branch of medicine that consists of the study, diagnosis, prevention, and treatment of diseases, disorders, and conditions of the oral cavity.</p>
    <a class="btn" href="#">Learn More <span class="arrow">›</span></a>
  </div>
  <div class="dots abs"><i class="on"></i><i></i><i></i><i></i></div>
</section>

<section class="about">
  <div class="about-photo abs" role="img" aria-label="Photo of a patient in the dental chair"></div>
  <div class="about-inset abs" role="img" aria-label="Photo of a dentist holding a tooth model"></div>
  <div class="about-copy abs">
    <h2 class="section-title">Our About Us</h2>
    <p class="about-text">Dentistry is often also understood to subsume the now largely defunct medical specialty of stomatology (the study of the mouth and its disorders and diseases) for which reason the two terms are used interchangeably in certain regions. For instance, in Australia, stomatology is considered to be a specialty of dentistry. However, some specialties such as oral and maxillofacial surgery (facial reconstruction) may require both.</p>
    <a class="btn" href="#">Learn More <span class="arrow">›</span></a>
  </div>
</section>

<section class="services abs">
  <h2 class="section-title">OUR SERVICES</h2>
</section>
<svg width="0" height="0" style="position:absolute">
  <symbol id="svc" viewBox="0 0 78 78"><circle cx="39" cy="39" r="36" fill="none" stroke="#555" stroke-width="2"/><path d="M27 30c4-6 20-6 24 0c2 5-1 10-3 14l-3 12c-1 2-3 2-4 0l-2-8l-2 8c-1 2-3 2-4 0l-3-12c-2-4-5-9-3-14z" fill="none" stroke="#555" stroke-width="2"/></symbol>
</svg>
<div class="service-card abs" style="left:232px;top:1452px"><svg class="service-icon"><use href="#svc"/></svg><div class="service-body"><div class="service-name">Rotline Exams</div><p class="service-text">I'm a paragraph. Click here to add your own text and edit me. It's easy.</p></div></div>
<div class="service-card abs" style="left:612px;top:1452px"><svg class="service-icon"><use href="#svc"/></svg><div class="service-body"><div class="service-name">Dental Hygiene</div><p class="service-text">I'm a paragraph. Click here to add your own text and edit me. It's easy.</p></div></div>
<div class="service-card abs" style="left:232px;top:1612px"><svg class="service-icon"><use href="#svc"/></svg><div class="service-body"><div class="service-name">Dental Fillings</div><p class="service-text">I'm a paragraph. Click here to add your own text and edit me. It's easy.</p></div></div>
<div class="service-card abs" style="left:612px;top:1612px"><svg class="service-icon"><use href="#svc"/></svg><div class="service-body"><div class="service-name">Dentures &amp; Veneers</div><p class="service-text">I'm a paragraph. Click here to add your own text and edit me. It's easy.</p></div></div>
<div class="service-card abs" style="left:232px;top:1768px"><svg class="service-icon"><use href="#svc"/></svg><div class="service-body"><div class="service-name">Emergency Dentistry</div><p class="service-text">I'm a paragraph. Click here to add your own text and edit me. It's easy.</p></div></div>
<div class="service-card abs" style="left:612px;top:1768px"><svg class="service-icon"><use href="#svc"/></svg><div class="service-body"><div class="service-name">Teeth Whitening</div><p class="service-text">I'm a paragraph. Click here to add your own text and edit me. It's easy.</p></div></div>

<h2 class="section-title dentists-title abs">Our Dentists</h2>
<div class="dentist abs" style="left:138px;top:2096px"><div class="dentist-photo" role="img" aria-label="Portrait of a dentist"></div><div class="dentist-name">Dr. Lena Hartley</div><div class="dentist-role">Tooth Specialist</div><a class="btn" href="#">Book Now</a></div>
<div class="dentist abs" style="left:450px;top:2096px"><div class="dentist-photo" role="img" aria-label="Portrait of a dentist"></div><div class="dentist-name">Dr. Marcus Reed</div><div class="dentist-role">Orthodontist</div><a class="btn" href="#">Book Now</a></div>
<div class="dentist abs" style="left:770px;top:2096px"><div class="dentist-photo" role="img" aria-label="Portrait of a dentist"></div><div class="dentist-name">Dr. Nora Ellison</div><div class="dentist-role">Hygienist</div><a class="btn" href="#">Book Now</a></div>

<h2 class="section-title contact-title abs">Contact Us</h2>
<div class="contact-col abs" style="left:210px;top:2612px"><h3>Our Address</h3><p>214 Alder Crest Lane</p><p>Brookvale, CA 95012</p><p>hello@bramblebay.example | Tel: 555-014-2286</p></div>
<div class="contact-divider abs"></div>
<div class="contact-col abs" style="left:630px;top:2612px"><h3>Opening Hours</h3><p>Monday - Friday &nbsp;9AM - 7PM</p><p style="margin-top:34px">Saturday &nbsp;9AM - 3PM</p></div>

<div class="map abs" role="img" aria-label="Street map showing the practice location"></div>
<div class="map-toggle abs"><span>Map</span><span>Satellite</span></div>
<div class="map-zoom abs"><span>+</span><span>−</span></div>

<footer class="site-footer abs">
  <div class="footer-brand abs"><span class="brand-mark"></span><span class="brand-name">Bramble Bay</span><div class="social"><i></i><i></i></div></div>
  <div class="footer-col abs" style="left:332px;top:24px"><h4>Quick Link</h4><p>Home<br>About<br>Service<br>Dentist<br>Contact</p></div>
  <div class="footer-col abs" style="left:520px;top:24px"><h4>Contact Us</h4><p>214 Alder Crest Lane<br>Brookvale, CA 95012<br>hello@bramblebay.example | Tel: 555-014-2286</p></div>
  <div class="footer-form abs">
    <div class="field">Email</div>
    <div class="field">Password</div>
    <div class="field tall">Message</div>
    <a class="btn" href="#">Submit</a>
  </div>
</footer>
<p class="copyright abs">© 2023 by Bramble Bay All Right Reserved.</p>

</body>
</html>
```